Need a powerful, eye-catching book cover design for a Public Relations book for Lawyers.

We need a beautiful, elegant, and professional cover for a public relations book. We’ll be selling this both to (1) creative, experienced legal marketers, and (2) conservative lawyers. It must grab their attention visually, and have a bold, easy to read headline. The cover image may wrap around to the back cover.SIZE: 6 x 9” 100 pagesTITLE: The Ultimate Public Relations Handbook for LawyersSUBHEAD: Make millions using media and the InternetCO-AUTHORSRoss Fishman, JDJohn HellermanInclude a CALLOUT quote: “The definitive PR book. Simple and powerful.” – Hal Brisket, SkaddenGRAPHICS:You may use one of the attached photos, crop or flip them however you’d like, or use something else entirely. DESCRIPTION for the back cover:Why do some law firms have the best reputations or command the highest hourly rates? Why are some the go-to firms or thought leaders in particular specialties? Why are your competitors in the media more than you? Two words: Public relations. The co-authors are known worldwide as leaders in public relations, legal marketing, and branding. Mark Tolliver is called, “A PR Guru.” Bar Ledger magazine wrote ““Many people consider Dale Warbeck to be the nation’s foremost expert on law firm marketing.”Hal Brisket built Valmont into the first firm to generate $1 billion in revenue. Nadine Cortez is the nation’s go-to lawyer for women’s issues. Your home town’s top PI lawyer gets the first look at the biggest cases. Why? Strategic, intentional, effective PR. Are you tired of toiling in anonymity? Want to earn the attention of reporters and editors who can build your credentials and reputation for expertise? Wouldn’t it be nice to have more clients begging you to represent them because they heard you were the best in town? That is what public relations is designed to do. Want to get more respect, earn more clients, and charge higher rates? Get known as a thought leader in a specialty practice or industry? Public relations could be your most-important marketing tool. And this book will teach you precisely how. Ready to catapult your practice to new heights? Take a deep breath and dive in….

Target Market(s)

1. Creative marketing professionals
2. Conservative 40-year-old lawyers

Industry/Entity Type

Legal

Font styles to use
Serif

Requirements
Must have
• Want a simple, bold, eye catching design conveying professionalism and quality. This is a practical, how-to book. We need a simple design and strong headline that will work well at a small thumbnail size on Quiverly.
Nice to have
• Perhaps the microphone could wrap around the cover? A tight crop of a microphone that creates an abstract could work. Let's create something memorable.

```html
<!DOCTYPE html>
<html lang="en">
<head>
<meta charset="utf-8">
<title>The Complete Press Outreach Guidebook for Attorneys – Cover Wrap</title>
<link rel="stylesheet" href="https://fonts.googleapis.com/css2?family=Bitter:wght@400;700;800&family=PT+Serif:wght@400;700&display=swap">
<style>
  :root {
    --page-bg: #eeece9;
    --paper: #ffffff;
    --tan-light: #e8cca2;
    --tan-dark: #dcba8a;
    --plum: #533868;
    --ink: #3e2f45;
    --white: #ffffff;
    --photo-light: #d9d2c6;
    --photo-mid: #b8b3ad;
    --photo-dark: #6f6c6a;
  }
  * { margin: 0; padding: 0; box-sizing: border-box; }
  html, body { width: 1200px; height: 800px; overflow: hidden; }
  body { background: var(--page-bg); position: relative; font-family: "PT Serif", serif; }

  .cover-wrap {
    position: absolute; left: 118px; top: 46px;
    width: 964px; height: 704px;
    background: var(--paper);
    box-shadow: 0 6px 20px rgba(0,0,0,0.12);
  }
  .panel {
    position: absolute; top: 12px; height: 680px; width: 448px;
    background: linear-gradient(160deg, var(--tan-light), var(--tan-dark));
  }
  .panel--back { left: 12px; }
  .panel--front { left: 504px; }

  .photo-area {
    position: absolute; z-index: 1;
    left: 432px; top: 168px; width: 428px; height: 362px;
    background: linear-gradient(135deg, var(--photo-light) 0%, var(--photo-mid) 55%, var(--photo-dark) 100%);
    border-radius: 6px;
  }

  .layer { position: absolute; z-index: 2; color: var(--plum); }

  .title { font-family: "Bitter", serif; }
  .title__lead { display: block; font-weight: 400; }
  .title__main { display: block; font-weight: 800; letter-spacing: 0.2px; }
  .title__rest { display: block; font-weight: 400; }
  .subhead { font-family: "Bitter", serif; font-weight: 400; color: var(--white); white-space: nowrap; }
  .authors { font-family: "PT Serif", serif; color: var(--ink); line-height: 1.2; }

  /* front */
  .front-title { left: 545px; top: 38px; line-height: 1.08; }
  .front-title .title__lead { font-size: 34px; }
  .front-title .title__main { font-size: 45px; }
  .front-title .title__rest { font-size: 33px; }
  .front-subhead { left: 545px; top: 168px; font-size: 18px; }
  .front-authors { left: 545px; top: 615px; font-size: 20px; }

  .callout {
    position: absolute; z-index: 2; left: 735px; top: 602px;
    width: 229px; height: 52px;
    background: var(--plum);
    clip-path: polygon(0 0, 100% 0, 100% 100%, 0 100%, 14px 50%);
    color: var(--white);
    font-family: "PT Serif", serif; font-size: 15px; line-height: 1.25;
    text-align: right; padding: 7px 22px 0 0;
  }
  .callout strong { font-weight: 700; }

  /* back */
  .back-title { left: 50px; top: 106px; line-height: 1.0; }
  .back-title .title__lead { font-size: 19px; }
  .back-title .title__main { font-size: 26px; }
  .back-title .title__rest { font-size: 19px; }
  .back-subhead { left: 50px; top: 178px; font-size: 10.5px; }
  .back-authors { left: 50px; top: 200px; font-size: 15px; }
  .back-blurb {
    left: 50px; top: 292px; width: 372px;
    font-size: 10.2px; line-height: 12.8px; color: var(--ink);
    text-align: justify; hyphens: auto;
  }

  /* spine */
  .spine-text {
    position: absolute; z-index: 2; left: 472px; width: 24px;
    writing-mode: vertical-rl;
    font-family: "PT Serif", serif; font-size: 11px; color: var(--plum);
    white-space: nowrap; line-height: 24px;
  }
  .spine-text--title { top: 16px; }
  .spine-text--title strong { font-weight: 700; }
  .spine-text--authors { top: 522px; color: var(--ink); }
</style>
</head>
<body>
  <main class="cover-wrap">
    <section class="panel panel--back" aria-label="Back cover"></section>
    <section class="panel panel--front" aria-label="Front cover"></section>

    <div class="photo-area" role="img" aria-label="Photo of a silver handheld microphone with a black cable, lying diagonally from the spine onto the front cover"></div>

    <h1 class="layer title front-title">
      <span class="title__lead">The Complete</span>
      <span class="title__main">Press Outreach</span>
      <span class="title__rest">Guidebook for Attorneys</span>
    </h1>
    <p class="layer subhead front-subhead">Make millions using media and the Internet</p>
    <p class="layer authors front-authors">Dale Warbeck,<br>JDMark Tolliver</p>
    <p class="callout"><strong>The definitive PR book.</strong><br>Simple and powerful.</p>

    <p class="spine-text spine-text--title"><strong>The Complete Press Outreach</strong> Guidebook for Attorneys</p>
    <p class="spine-text spine-text--authors">Dale Warbeck, JDMark Tolliver</p>

    <h2 class="layer title back-title">
      <span class="title__lead">The Complete</span>
      <span class="title__main">Press Outreach</span>
      <span class="title__rest">Guidebook for Attorneys</span>
    </h2>
    <p class="layer subhead back-subhead">Make millions using media and the Internet</p>
    <p class="layer authors back-authors">Dale Warbeck &amp;<br>JDMark Tolliver</p>
    <p class="layer back-blurb">Why do some law firms have the best reputations or command the highest hourly rates? Why are some the go-to firms or thought leaders in particular specialties? Why are your competitors in the media more than you? Two words: Public relations. The co-authors are known worldwide as leaders in public relations, legal marketing, and branding. Mark Tolliver is called, “A PR Guru.” Bar Ledger magazine wrote “Many people consider Dale Warbeck to be the nation’s foremost expert on law firm marketing.” Hal Brisket built Valmont into the first firm to generate $1 billion in revenue. Nadine Cortez is the nation’s go-to lawyer for women’s issues. Your home town’s top PI lawyer gets the first look at the biggest cases. Why? Strategic, intentional, effective PR. Are you tired of toiling in anonymity? Want to earn the attention of reporters and editors who can build your credentials and reputation for expertise? Wouldn’t it be nice to have more clients begging you to represent them because they heard you were the best in town? That is what public relations is designed to do. Want to get more respect, earn more clients, and charge higher rates? Get known as a thought leader in a specialty practice or industry? Public relations could be your most-important marketing tool. And this book will teach you precisely how. Ready to catapult your practice to new heights? Take a deep breath and dive in...</p>
  </main>
</body>
</html>
```